Shipping and Logistics, Project

Project description : Company Profile

A total logistics company covering domestic / international freight forwarding, warehouse management services, haulage, supply chain management, transport management & distribution, procurement & assembly services, shipping, chartering & bunker services, project logistics & tax exemption consultancy, oil & gas logistics, halal logistics services & integrated logistics management. We’re a well-established and experienced freight forwarder in Kuala Lumpur, Malaysia. We specialize in customized value-added solution that optimizes your supply chain by trimming inventory, reducing logistics cost and enhancing your customer service levels.

As a member of the Continental Parcel and Carriage Alliance which comprise of 170 global freight agents in 80 countries that promotes great handling in cross-trade logistics and freighting. You could rely on our efficiency in handlings of export cargo (FCL, LCL, Bulk and Conventional) between our global network offices worldwide with a total scale of 10,000 groomed specialists in various logistics division working together to ensure delivery task meets with your expectation. With our dedicated qualified and experienced professionals, we are fully committed to serving our clients.

Our generic services are listed below for your reference:

• Air Freight
• Ocean Freight FCL & LCL
• Container Haulage
• Warehousing
• Transportation and Distribution within Malaysia and Thailand
• Cross-Border Road Line-hauls between Thailand, Malaysia, Singapore and Laos
• Customs Brokerage and Forwarding
• Project Cargo Freight Forwarding for setting up of new plants / factories and ad hoc heavy-lift
• Air-Sea-Road-Rail multi-modal options
• Import / Export / Storage / Documentation / Handling of DG / Hazmat
• Vessel and Aircraft Charters

Our Mission
Based on the motto “Quick, Reliable and Polite”, we are dedicated to upholding the following three points corporate philosophy:
1. Adhering to the principle that “the customer always comes first”.
2. Contributing to the development of the local community.
3. Making it our duty to be responsible and sincere.

Our Edge
• One-Stop Logistics Solutions
• Extensive Network Throughout Malaysia
• Highly Qualified and Experienced Pool of Professionals
• Comprehensive IT Solutions
• Innovative and Customer-focused Solutions
• Flexible and Consistent in Managing Exceptions
• Total Supply Chain Visibility

Target Market
1. We sell the logistics services to all the industry in Malaysia and Worldwide. (ONE Stop Logistics Solutions)

Competitor
1. RT Vollmark
2. Corventa Transport
3. Brastow + Feld
4. TOLRI
5. QVN
6. Trundelles
7. Wiro Logistics

Rules for Picking a Company Name
1. Unique and unforgettable
2. Avoid unusual spellings
3. Easy to pronounce and remember
4. Keep it simple
5. Make some sense
6. Give a clue

Rules for Picking a Company Logo
4. Keep it simple
5. Make some sense
6. Give a clue

1. Simplicity
2. Memorability
3. Originality
4. Modern Yet Timeless
5. Balance
6. Complementary
7. Versatility

Stationery Information
1. Company Name : Tenhaul Solutions Sdn Bhd
2. Company Registration : 2738516-P
3. Address : 42-07, Jalan Seri Dedap 5, Taman Bukit Kenari, 81100 Johor Bahru, Johor, Malaysia.
4. Name : Derek Tan
5. Position : Manager
6. Mobile No : (+6019) 4183907
7. Office No : (+607) 2918476
8. Fax No : Not Available
9. Email Address : derek.tan@tenhaul-solutions.example
10. Web Domain : www.tenhaul-solutions.example
11. Company Slogan : Be Globally Connected

Target Market(s)

Corporate Company

Industry/Entity Type

Shipping and Logistics Industry

Requirements
Must have
• Company Full Name : TENHAUL SOLUTIONS SDN. BHD.
Nice to have
• Keep it simple and unforgettable ...

```html
<!DOCTYPE html>
<html lang="en">
<head>
<meta charset="utf-8">
<title>Tenhaul Solutions Stationery</title>
<link rel="stylesheet" href="https://fonts.googleapis.com/css2?family=Poppins:wght@400;500;600&display=swap">
<style>
  :root {
    --backdrop: #c8c8c8;
    --paper: #ffffff;
    --brand-blue: #3c88c8;
    --watermark: rgba(60, 136, 200, 0.11);
    --ink: #222222;
    --ink-soft: #333333;
  }
  * { margin: 0; padding: 0; box-sizing: border-box; }
  html, body { width: 1200px; height: 900px; overflow: hidden; }
  body {
    background: var(--backdrop);
    font-family: "Poppins", sans-serif;
    color: var(--ink);
    position: relative;
  }
  .sheet { position: absolute; background: var(--paper); overflow: hidden; }

  /* faint background area */
  .watermark {
    position: absolute;
    background: radial-gradient(ellipse at center, var(--watermark) 0%, var(--watermark) 45%, rgba(60,136,200,0) 72%);
  }

  /* brand lockup */
  .brand { position: absolute; display: flex; align-items: center; z-index: 1; }
  .brand-square { background: var(--brand-blue); flex: none; }
  .brand-text { display: flex; flex-direction: column; line-height: 1; color: var(--ink); }
  .brand-name { font-weight: 500; }
  .brand-sub { font-weight: 500; }

  /* folder */
  .folder { left: 114px; top: 145px; width: 314px; height: 436px; }
  .folder .watermark { left: 0; top: 67px; width: 314px; height: 336px; }
  .folder .brand { left: 62px; top: 20px; gap: 10px; }
  .folder .brand-square { width: 42px; height: 42px; }
  .folder .brand-name { font-size: 26px; letter-spacing: 0.5px; }
  .folder .brand-sub { font-size: 9px; letter-spacing: 2.2px; margin-top: 5px; }
  .folder-band {
    position: absolute; left: 0; bottom: 0; width: 100%; height: 33px;
    background: var(--brand-blue); color: var(--paper);
    display: flex; align-items: center; justify-content: center;
    font-size: 11px; letter-spacing: 1.6px; z-index: 1;
  }

  /* letterhead */
  .letterhead { left: 460px; top: 154px; width: 291px; height: 425px; }
  .letterhead .watermark { left: 34px; top: 102px; width: 219px; height: 252px; }
  .letterhead .brand { left: 23px; top: 17px; gap: 6px; }
  .letterhead .brand-square { width: 24px; height: 24px; }
  .letterhead .brand-name { font-size: 12.5px; }
  .letterhead .brand-sub { font-size: 5.2px; letter-spacing: 0.8px; margin-top: 2.5px; }
  .contact {
    position: absolute; right: 21px; top: 22px; text-align: right;
    font-size: 5px; line-height: 6.2px; color: var(--ink-soft); z-index: 1;
  }
  .contact .label { color: var(--brand-blue); }
  .letter-footer { position: absolute; left: 21px; right: 21px; bottom: 10px; font-size: 5px; color: var(--ink-soft); z-index: 1; }
  .footer-row { display: flex; justify-content: space-between; padding: 0 3px 3px; border-bottom: 0.7px solid var(--brand-blue); }
  .footer-row .slogan { color: var(--brand-blue); }
  .footer-address { text-align: center; margin-top: 4px; }

  /* envelopes */
  .flap { position: absolute; display: block; }
  .envelope-large { left: 786px; top: 151px; width: 308px; height: 431px; }
  .envelope-large .watermark { left: 53px; top: 113px; width: 205px; height: 236px; }
  .envelope-large .brand { left: 25px; top: 37px; gap: 6px; }
  .envelope-large .brand-square { width: 22px; height: 22px; }
  .envelope-large .brand-name { font-size: 11.5px; }
  .envelope-large .brand-sub { font-size: 4.8px; letter-spacing: 0.7px; margin-top: 2px; }
  .envelope-large .address {
    position: absolute; left: 0; right: 0; top: 411px; text-align: center;
    font-size: 5px; color: var(--ink-soft); z-index: 1;
  }

  .envelope-small { left: 436px; top: 650px; width: 340px; height: 170px; }
  .envelope-small .watermark { left: 203px; top: 23px; width: 130px; height: 147px; }
  .envelope-small .brand { left: 17px; top: 23px; gap: 5px; }
  .envelope-small .brand-square { width: 20px; height: 20px; }
  .envelope-small .brand-name { font-size: 10.5px; }
  .envelope-small .brand-sub { font-size: 4.5px; letter-spacing: 0.6px; margin-top: 2px; }
  .envelope-small .address {
    position: absolute; left: 19px; top: 137px;
    font-size: 5.4px; line-height: 6.5px; color: var(--ink-soft); z-index: 1;
  }
</style>
</head>
<body>

  <!-- presentation folder -->
  <section class="sheet folder">
    <div class="watermark" role="img" aria-label="Faint brand background area"></div>
    <div class="brand">
      <span class="brand-square"></span>
      <div class="brand-text">
        <span class="brand-name">TENHAUL</span>
        <span class="brand-sub">SOLUTIONS SDN. BHD.</span>
      </div>
    </div>
    <div class="folder-band">BE GLOBALLY CONNECTED</div>
  </section>

  <!-- letterhead -->
  <section class="sheet letterhead">
    <div class="watermark" role="img" aria-label="Faint brand background area"></div>
    <div class="brand">
      <span class="brand-square"></span>
      <div class="brand-text">
        <span class="brand-name">TENHAUL</span>
        <span class="brand-sub">SOLUTIONS SDN. BHD.</span>
      </div>
    </div>
    <div class="contact">
      <div><span class="label">P:</span> (+6019) 418 3907</div>
      <div><span class="label">M:</span> +607) 291 8476</div>
      <div><span class="label">E:</span> derek.tan@tenhaul-solutions.example</div>
    </div>
    <div class="letter-footer">
      <div class="footer-row">
        <span>Company No. 2738516-P &nbsp;| &nbsp;<span class="slogan">BE GLOBALLY CONNECTED</span></span>
        <span>www.tenhaul-solutions.example</span>
      </div>
      <div class="footer-address">42-07, Jalan Seri Dedap 5 Taman Bukit Kenari, 81100, Johor,Bahru Johor, Malaysia.</div>
    </div>
  </section>

  <!-- large envelope -->
  <svg class="flap" style="left:786px; top:94px;" width="308" height="61" viewBox="0 0 308 61" aria-hidden="true">
    <polygon points="0,54 33,0 270,0 308,53 308,61 0,57" fill="var(--brand-blue)"/>
  </svg>
  <section class="sheet envelope-large">
    <div class="watermark" role="img" aria-label="Faint brand background area"></div>
    <div class="brand">
      <span class="brand-square"></span>
      <div class="brand-text">
        <span class="brand-name">TENHAUL</span>
        <span class="brand-sub">SOLUTIONS SDN. BHD.</span>
      </div>
    </div>
    <div class="address">42-07, Jalan Seri Dedap 5, Taman Bukit Kenari, 81100 Johor,Bahru, Johor, Malaysia.</div>
  </section>

  <!-- DL envelope -->
  <svg class="flap" style="left:436px; top:623px;" width="340" height="27" viewBox="0 0 340 27" aria-hidden="true">
    <polygon points="0,27 15,0 322,0 340,27" fill="var(--brand-blue)"/>
  </svg>
  <section class="sheet envelope-small">
    <div class="watermark" role="img" aria-label="Faint brand background area"></div>
    <div class="brand">
      <span class="brand-square"></span>
      <div class="brand-text">
        <span class="brand-name">TENHAUL</span>
        <span class="brand-sub">SOLUTIONS SDN. BHD.</span>
      </div>
    </div>
    <div class="address">
      42-07, Jalan Seri Dedap 5,<br>
      Taman Bukit Kenari, 81100 Johor<br>
      Bahru, Johor, Malaysia.
    </div>
  </section>

</body>
</html>
```